Business Card, Stationary, & Folder for Mortgage Company
KLD Mortgage
Business Card, Stationary, & Folder for Mortgage Company - Real Estate
Creative Brief
Professional
Terrin Balk
Senior Loan Officer
4186 Orchard Crest Blvd, #209 Takoma Park, Maryland 20912
tbalk@kldmortgage-example.com
www.KLDMortgage-example.com
I would like to use the colors in the logo but would like to also add a touch of red. I also would like to use the symbols for the phone numbers, email, and website
KLDMortgage KLDMortgage
I am looking for just a touch of red in the design. The main design should match the colors of the logo. Please don't alter the logo.
PixelHarborLab PixelHarborLab

```html
<!DOCTYPE html>
<html lang="en">
<head>
<meta charset="utf-8">
<title>KLD Mortgage – Stationery Set</title>
<link rel="stylesheet" href="https://fonts.googleapis.com/css2?family=Open+Sans:wght@400;600;700&display=swap">
<style>
:root{
  --stage:#6e93a9;
  --paper:#ffffff;
  --band:#9b9c9e;
  --band-dark:#7d7e80;
  --brand:#1f4d9b;
  --ink:#2b2b2b;
  --soft:#8a8a8a;
  --accent:#c8202f;
  --night:#1b1b1d;
  --faint:#d6dde8;
}
*{box-sizing:border-box;margin:0;padding:0}
html,body{width:1200px;height:967px;overflow:hidden}
body{background:var(--stage);font-family:"Open Sans",Arial,sans-serif;color:var(--ink);position:relative}
.piece{position:absolute;background:var(--paper);box-shadow:0 6px 14px rgba(0,0,0,.25)}
.brand{display:flex;align-items:center;gap:5px;font-weight:700;color:var(--brand);white-space:nowrap}
.brand .dot{border-radius:50%;background:var(--brand);flex:none}
.contact{font-size:6px;line-height:1.55;color:var(--ink);white-space:nowrap}
.contact .name{font-weight:700;font-size:7.5px}
.band{background:var(--band)}
.redline{height:1px;background:var(--accent)}

/* business cards */
.card{width:200px;height:116px}
.card-front .band{position:absolute;right:0;top:0;width:124px;height:116px;padding:14px 6px}
.card-front .band .contact{color:#fff}
.card-front .brand{position:absolute;left:5px;top:52px;font-size:7.5px}
.card-back{background:var(--band)}
.card-back .brand{position:absolute;inset:0;justify-content:center;color:#fff;font-size:13px}
.card-back .brand .dot{background:#fff}
.card-white .brand{position:absolute;inset:0;justify-content:center;font-size:13px}
.card-white .redline{position:absolute;left:0;right:0;bottom:10px}

/* letterhead */
.letterhead{left:228px;top:125px;width:290px;height:380px}
.letterhead .top{height:40px;display:flex;align-items:center;justify-content:space-between;padding:0 10px}
.letterhead .top .band{width:196px;height:26px;padding:4px 6px}
.letterhead .top .band .contact{color:#fff;font-size:5px;line-height:1.5}
.letterhead .watermark{position:absolute;left:0;right:0;top:150px;display:flex;justify-content:center;font-weight:700;font-size:36px;color:var(--faint);white-space:nowrap}
.letterhead .redline{position:absolute;left:12px;right:12px;bottom:16px}

/* small cards pair */
.mini{width:140px;height:80px}
.mini .band{position:absolute;right:0;top:0;width:76px;height:80px;padding:8px 6px}
.mini .band .contact{color:#fff;font-size:5px}
.mini .brand{position:absolute;left:5px;top:35px;font-size:6px;gap:3px}

/* DL envelope */
.dl{left:560px;top:285px;width:300px;height:120px}
.dl .band{position:absolute;right:0;top:0;width:180px;height:22px}
.dl .brand{position:absolute;left:12px;top:12px;font-size:9px}
.dl .redline{position:absolute;left:0;right:0;bottom:10px}

/* envelopes stack */
.env{width:330px;height:110px;overflow:hidden}
.env svg{position:absolute;left:0;top:0}
.env .brand{position:absolute;left:0;right:0;top:14px;justify-content:center;font-size:10px;color:#fff}
.env .brand .dot{background:#fff}
.env-white .brand{color:var(--brand)}
.env-white .brand .dot{background:var(--brand)}

/* fax */
.fax{left:830px;top:420px;width:330px;height:345px;padding:18px 20px}
.fax .band{position:absolute;left:0;right:0;top:0;height:30px}
.fax .brand{position:absolute;right:14px;top:8px;font-size:9px;color:#fff}
.fax .brand .dot{background:#fff}
.fax h1{margin-top:30px;font-size:30px;font-weight:700;color:var(--night)}
.fax .row{display:flex;gap:6px;font-size:8px;margin-top:10px;align-items:flex-end}
.fax .row .fill{flex:1;border-bottom:1px solid var(--soft);height:9px}
.fax .checks{display:flex;gap:14px;font-size:7px;margin-top:16px}
.fax .checks span::before{content:"";display:inline-block;width:7px;height:7px;border:1px solid var(--soft);margin-right:3px;vertical-align:-1px}
.fax .redline{position:absolute;left:20px;right:20px;bottom:18px}

/* folder */
.folder{left:110px;top:548px;width:500px;height:410px;background:none;box-shadow:none}
.folder svg{position:absolute;left:0;top:0}
.folder .brand-main{position:absolute;left:300px;top:118px;font-size:20px}
.folder .card-slot{position:absolute;left:208px;top:366px;font-size:6px;gap:3px}

/* disc */
.disc{left:650px;top:455px;width:120px;height:120px;border-radius:50%;background:radial-gradient(circle,#fff 0 9px,var(--band) 10px 18px,#fff 19px)}
.disc .brand{position:absolute;left:0;right:0;top:28px;justify-content:center;font-size:8px}
.sleeve{left:645px;top:590px;width:200px;height:205px}
.sleeve .band{height:30px}
.sleeve .brand{position:absolute;inset:30px 0 0;justify-content:center;font-size:13px}
.sleeve .redline{position:absolute;left:0;right:0;bottom:12px}
</style>
</head>
<body>

<div class="piece card card-front" style="left:20px;top:160px">
  <div class="brand"><span class="dot" style="width:9px;height:9px"></span>KLD Mortgage</div>
  <div class="band">
    <div class="contact">
      <div class="name">Terrin Balk</div>
      <div>Senior Loan Officer</div>
      <div>Office 301.555.0148</div>
      <div>Mobile 301.555.0177</div>
      <div>tbalk@kldmortgage-example.com</div>
      <div>www.KLDMortgage-example.com</div>
    </div>
  </div>
</div>

<div class="piece card card-white" style="left:30px;top:290px">
  <div class="brand"><span class="dot" style="width:14px;height:14px"></span>KLD Mortgage</div>
  <div class="redline"></div>
</div>

<div class="piece card card-back" style="left:40px;top:420px">
  <div class="brand"><span class="dot" style="width:14px;height:14px"></span>KLD Mortgage</div>
</div>

<div class="piece letterhead">
  <div class="top">
    <div class="brand" style="font-size:7px;gap:3px"><span class="dot" style="width:8px;height:8px"></span>KLD Mortgage</div>
    <div class="band"><div class="contact">4186 Orchard Crest Blvd, #209 Takoma Park, Maryland 20912<br>tbalk@kldmortgage-example.com · www.KLDMortgage-example.com</div></div>
  </div>
  <div class="watermark">KLD Mortgage</div>
  <div class="redline"></div>
</div>

<div class="piece mini" style="left:545px;top:120px">
  <div class="brand"><span class="dot" style="width:6px;height:6px"></span>KLD Mortgage</div>
  <div class="band"><div class="contact"><b>Terrin Balk</b><br>Senior Loan Officer<br>Office 301.555.0148</div></div>
</div>
<div class="piece mini" style="left:560px;top:190px">
  <div class="brand"><span class="dot" style="width:6px;height:6px"></span>KLD Mortgage</div>
  <div class="band"><div class="contact"><b>Terrin Balk</b><br>Senior Loan Officer<br>Mobile 301.555.0177</div></div>
</div>

<div class="piece dl">
  <div class="band"></div>
  <div class="brand"><span class="dot" style="width:9px;height:9px"></span>KLD Mortgage</div>
  <div class="redline"></div>
</div>

<div class="piece env" style="left:820px;top:60px">
  <svg width="330" height="110"><polygon points="0,0 330,0 165,48" fill="var(--brand)"/><rect width="330" height="4" fill="var(--brand)"/></svg>
  <div class="brand"><span class="dot" style="width:9px;height:9px"></span>KLD Mortgage</div>
</div>
<div class="piece env" style="left:830px;top:160px">
  <svg width="330" height="110"><polygon points="0,0 330,0 165,48" fill="var(--night)"/></svg>
  <div class="brand"><span class="dot" style="width:9px;height:9px"></span>KLD Mortgage</div>
</div>
<div class="piece env env-white" style="left:840px;top:260px">
  <svg width="330" height="110"><polyline points="0,0 165,48 330,0" fill="none" stroke="#d0d0d0"/></svg>
  <div class="brand" style="top:52px"><span class="dot" style="width:9px;height:9px"></span>KLD Mortgage</div>
</div>

<div class="piece fax">
  <div class="band"></div>
  <div class="brand"><span class="dot" style="width:9px;height:9px"></span>KLD Mortgage</div>
  <h1>Fax</h1>
  <div class="row"><span>To:</span><span class="fill"></span><span>From:</span><span class="fill"></span></div>
  <div class="row"><span>Fax:</span><span class="fill"></span><span>Phone:</span><span class="fill"></span></div>
  <div class="row"><span>Date:</span><span class="fill"></span><span>Pages:</span><span class="fill"></span></div>
  <div class="row"><span>Re:</span><span class="fill"></span></div>
  <div class="checks"><span>Urgent</span><span>For Review</span><span>Please Comment</span></div>
  <div class="redline"></div>
</div>

<div class="piece folder">
  <svg width="500" height="410" viewBox="0 0 500 410">
    <path d="M20 28 Q20 0 48 0 H452 Q480 0 480 28 V32 H20 Z" fill="var(--band-dark)"/>
    <rect x="0" y="32" width="500" height="26" fill="var(--band)"/>
    <rect x="20" y="58" width="460" height="180" fill="var(--paper)"/>
    <line x1="20" y1="230" x2="480" y2="230" stroke="var(--accent)" stroke-width="1"/>
    <path d="M20 238 H480 V290 L445 325 H285 V410 H215 V325 H55 L20 290 Z" fill="var(--band)"/>
    <line x1="20" y1="238" x2="480" y2="238" stroke="#858688"/>
    <rect x="200" y="345" width="100" height="50" fill="var(--paper)"/>
  </svg>
  <div class="brand brand-main"><span class="dot" style="width:22px;height:22px"></span>KLD Mortgage</div>
  <div class="brand card-slot"><span class="dot" style="width:6px;height:6px"></span>KLD Mortgage</div>
</div>

<div class="piece disc"><div class="brand"><span class="dot" style="width:7px;height:7px"></span>KLD Mortgage</div></div>
<div class="piece sleeve">
  <div class="band"></div>
  <div class="brand"><span class="dot" style="width:13px;height:13px"></span>KLD Mortgage</div>
  <div class="redline"></div>
</div>

</body>
</html>
```